Business card design needed

Chasing a very simplistic modern design with a logo incorporating "TRV".
I'm starting a plumbing business.
I do water, sanitary and drainage plumbing that will cover residential, commercial, rental, rural, excavation, new housing and all maintanence requirements.

Industry/Entity Type

Business

Contact Information for Business Card

TRV PLUMBING SERVICES
DEAN HOLLOWBY - LICENSED PLUMBER
PHONE: 0481926574
E-MAIL: hollodt7@wirelane.com
NORTHERN SUBURBS

Requirements
Must have
• lower case email address

```html
<!DOCTYPE html>
<html lang="en">
<head>
<meta charset="utf-8">
<title>TRV Plumbing Services – Business Card</title>
<link rel="stylesheet" href="https://fonts.googleapis.com/css2?family=Exo+2:wght@600;700;800&family=Ubuntu:wght@400;500&display=swap">
<style>
  :root {
    --stage: #e9ebee;
    --card-dark: #141516;
    --card-dark-2: #26282a;
    --brand-blue: #2f8fd0;
    --brand-blue-deep: #1f6fa8;
    --paper: #ffffff;
    --paper-shade: #e4e6e8;
    --ink: #1b1c1e;
    --ink-soft: #2c2e31;
    --white: #ffffff;
  }
  * { box-sizing: border-box; margin: 0; padding: 0; }
  html, body { width: 1200px; height: 861px; overflow: hidden; }
  body {
    background: var(--stage);
    display: flex;
    align-items: center;
    justify-content: center;
    gap: 40px;
  }
  .card {
    position: relative;
    width: 540px;
    height: 330px;
    border-radius: 16px;
    overflow: hidden;
    background: linear-gradient(180deg, var(--paper) 0%, var(--paper-shade) 100%);
    box-shadow: 0 10px 26px rgba(0,0,0,0.18);
    display: flex;
    flex-direction: column;
  }
  .card__top {
    position: relative;
    display: flex;
    flex-direction: column;
    align-items: center;
    justify-content: center;
    border-bottom: 7px solid var(--brand-blue);
  }
  .card__texture {
    position: absolute;
    inset: 0;
    background: radial-gradient(ellipse at 50% 30%, var(--card-dark-2) 0%, var(--card-dark) 75%);
  }
  .logo { position: relative; text-align: center; }
  .logo__name {
    font-family: "Exo 2", sans-serif;
    font-weight: 800;
    color: var(--brand-blue);
    line-height: 0.9;
    letter-spacing: 2px;
  }
  .logo__tagline {
    font-family: "Exo 2", sans-serif;
    font-weight: 700;
    color: var(--white);
    letter-spacing: 4px;
  }

  /* Front */
  .card--front .card__top { height: 228px; }
  .card--front .logo__name { font-size: 118px; }
  .card--front .logo__tagline { font-size: 28px; margin-top: 4px; }
  .services {
    flex: 1;
    display: flex;
    flex-direction: column;
    align-items: center;
    justify-content: center;
    text-align: center;
    font-family: "Ubuntu", sans-serif;
    color: var(--ink);
    font-size: 17px;
    line-height: 1.4;
  }
  .services__title { font-weight: 500; font-size: 18px; }

  /* Back */
  .card--back .card__top { height: 192px; }
  .card--back .logo__name { font-size: 96px; }
  .card--back .logo__tagline { font-size: 23px; margin-top: 4px; }
  .details {
    flex: 1;
    display: flex;
    align-items: center;
    justify-content: space-between;
    padding: 0 20px 0 20px;
  }
  .person {
    border-left: 7px solid var(--brand-blue);
    padding-left: 10px;
    font-family: "Ubuntu", sans-serif;
    color: var(--ink);
  }
  .person__name { font-size: 27px; font-weight: 500; letter-spacing: 0.5px; line-height: 1.1; }
  .person__role { font-size: 18px; color: var(--ink-soft); letter-spacing: 0.5px; }
  .contact {
    list-style: none;
    font-family: "Ubuntu", sans-serif;
    font-size: 15.5px;
    color: var(--ink);
    text-align: right;
  }
  .contact__item {
    display: flex;
    align-items: center;
    justify-content: flex-end;
    gap: 6px;
    line-height: 30px;
  }
  .contact__icon { width: 20px; height: 20px; flex: none; }
</style>
</head>
<body>

  <section class="card card--front" aria-label="Business card front">
    <div class="card__top">
      <div class="card__texture" role="img" aria-label="Dark embossed pyramid texture"></div>
      <div class="logo">
        <div class="logo__name">TRV</div>
        <div class="logo__tagline">PLUMBING SERVICES</div>
      </div>
    </div>
    <div class="services">
      <p class="services__title">Water, Sanitary and Drainage Plumbing</p>
      <p>(Residential, Commercial, Rental, Rural, Excavation,<br>New housing and All Maintanence Requirements)</p>
    </div>
  </section>

  <section class="card card--back" aria-label="Business card back">
    <div class="card__top">
      <div class="card__texture" role="img" aria-label="Dark embossed pyramid texture"></div>
      <div class="logo">
        <div class="logo__name">TRV</div>
        <div class="logo__tagline">PLUMBING SERVICES</div>
      </div>
    </div>
    <div class="details">
      <div class="person">
        <p class="person__name">DEAN HOLLOWBY</p>
        <p class="person__role">LICENSED PLUMBER</p>
      </div>
      <ul class="contact">
        <li class="contact__item">0481926574
          <svg class="contact__icon" viewBox="0 0 20 20" aria-hidden="true">
            <circle cx="10" cy="10" r="8.5" fill="none" stroke="var(--brand-blue-deep)" stroke-width="1.6"/>
            <path d="M6.5 6.5c0 4 3 7 7 7l1-1.6-2-1-1 .9c-1.3-.6-2.3-1.6-2.9-2.9l.9-1-1-2z" fill="var(--brand-blue-deep)"/>
          </svg>
        </li>
        <li class="contact__item">hollodt7@wirelane.com
          <svg class="contact__icon" viewBox="0 0 20 20" aria-hidden="true">
            <circle cx="10" cy="10" r="8.5" fill="none" stroke="var(--brand-blue-deep)" stroke-width="1.6"/>
            <rect x="5.5" y="7" width="9" height="6.2" rx="0.8" fill="var(--brand-blue-deep)"/>
            <path d="M5.8 7.4l4.2 3.2 4.2-3.2" fill="none" stroke="var(--white)" stroke-width="1"/>
          </svg>
        </li>
        <li class="contact__item">Northern Suburbs
          <svg class="contact__icon" viewBox="0 0 20 20" aria-hidden="true">
            <circle cx="10" cy="10" r="8.5" fill="none" stroke="var(--brand-blue-deep)" stroke-width="1.6"/>
            <path d="M10 15.5s-3.8-4-3.8-6.6a3.8 3.8 0 0 1 7.6 0c0 2.6-3.8 6.6-3.8 6.6z" fill="var(--brand-blue-deep)"/>
            <circle cx="10" cy="8.9" r="1.4" fill="var(--white)"/>
          </svg>
        </li>
      </ul>
    </div>
  </section>

</body>
</html>
```